Letterhead & Business Card for our Professional Practice (Financial Services)

We are looking for someone to design a letterhead and business card for our business, which is a professional practice called Harbor Lumen Capital Limited. The website is at www.harborrlumencapital.example.co.uk.

The letterhead needs to have: (a) our logo (b) address (c) telephone number (d) email address and (e) our company number.

We would like the stationary to be consistent with the website.

I have attached the logo in EPS and PNG format.

Target Market(s)

Professional services, large commercial enterprises, financial services

Industry/Entity Type

Financial Service

Font styles to use
Serif

Colors
3176b5
f04a50

Requirements
Must have
• Be consistent with our website located at www.harborlumencapital.example.co.uk
• Be in the following formats:
• 1. Word template for the letterhead
• 2. PDF for the letterhead with setup and bleeds required at www.presskite.example.co.uk
• 3. PDF for the business card with setup and bleeds required at www.presskite.example.co.uk
Nice to have
• Something with a really interesting design that says "these guys are professional but dynamic and interesting"
Should not have
• Boring

```html
<!DOCTYPE html>
<html lang="en">
<head>
<meta charset="utf-8">
<title>Harbor Lumen Capital – Business Card</title>
<link rel="stylesheet" href="https://fonts.googleapis.com/css2?family=Arimo:wght@400;700&display=swap">
<style>
  :root {
    --navy: #0f4a85;
    --navy-deep: #0a3a6c;
    --red: #e2384d;
    --ink: #1d4f8c;
    --grey: #6f7378;
    --paper: #ffffff;
    --backdrop: #2b2d30;
  }
  * { box-sizing: border-box; margin: 0; padding: 0; }
  html, body {
    width: 1200px; height: 950px; overflow: hidden;
    background: var(--backdrop);
    font-family: "Arimo", Arial, sans-serif;
  }
  .stage {
    width: 1200px; height: 950px;
    display: flex; flex-direction: column; align-items: center; justify-content: center;
    gap: 50px;
  }
  .card {
    position: relative;
    width: 700px; height: 400px;
    overflow: hidden;
  }

  /* Front */
  .card-front {
    background: linear-gradient(160deg, var(--navy) 0%, var(--navy-deep) 100%);
    color: var(--paper);
    display: flex; flex-direction: column; align-items: center; justify-content: center;
  }
  .brand {
    display: flex; align-items: center; gap: 14px;
  }
  .brand-mark {
    width: 46px; height: 46px; flex: none;
  }
  .brand-name {
    font-size: 34px; font-weight: 700; letter-spacing: 0.2px;
  }
  .card-front .brand-mark { background: var(--paper); }
  .front-web {
    margin-top: 44px;
    font-size: 15px; letter-spacing: 3.2px;
  }

  /* Back */
  .card-back { background: var(--paper); }
  .card-back .brand {
    position: absolute; right: 40px; top: 120px;
  }
  .card-back .brand-mark { background: var(--red); width: 40px; height: 40px; }
  .card-back .brand-name { color: var(--ink); font-size: 30px; }

  .accent-tab {
    position: absolute; left: 0; top: 148px;
    width: 14px; height: 52px; background: var(--red);
  }
  .person { position: absolute; left: 42px; top: 148px; }
  .person-name { color: var(--ink); font-size: 23px; font-weight: 700; }
  .person-role { color: var(--red); font-size: 18px; margin-top: 4px; }

  .address {
    position: absolute; left: 108px; top: 226px;
    color: var(--grey); font-size: 17px; line-height: 1.3;
  }
  .contacts {
    position: absolute; left: 108px; top: 300px;
    list-style: none; color: var(--grey); font-size: 17px;
  }
  .contacts li { display: flex; align-items: center; gap: 12px; height: 26px; }
  .contacts svg { width: 16px; height: 16px; flex: none; fill: var(--ink); }

  .band-blue {
    position: absolute; left: 0; bottom: 0;
    width: 430px; height: 12px; background: var(--ink);
  }
  .band-red {
    position: absolute; left: 430px; bottom: 0;
    width: 270px; height: 12px; background: var(--red);
  }
</style>
</head>
<body>
<main class="stage">

  <section class="card card-front" aria-label="Business card front">
    <div class="brand">
      <span class="brand-mark"></span>
      <span class="brand-name">Harbor Lumen Capital</span>
    </div>
    <p class="front-web">www.harborrlumencapital.example.co.uk</p>
  </section>

  <section class="card card-back" aria-label="Business card back">
    <span class="accent-tab"></span>
    <div class="person">
      <p class="person-name">Elias Varno</p>
      <p class="person-role">President</p>
    </div>

    <address class="address">
      2170 Ashgrove<br>Drive, Cedar Bend<br>NY 10984
    </address>

    <ul class="contacts">
      <li>
        <svg viewBox="0 0 16 16" aria-hidden="true"><path d="M3.5 1.5l2.5 3-1.5 1.8a9 9 0 0 0 5.2 5.2l1.8-1.5 3 2.5-1.6 2a2 2 0 0 1-2 .5A13 13 0 0 1 1 5.1a2 2 0 0 1 .5-2z"/></svg>
        555 0142 7781
      </li>
      <li>
        <svg viewBox="0 0 16 16" aria-hidden="true"><path d="M1 3h14v10H1z M2 4l6 5 6-5" fill="none" stroke="#1d4f8c" stroke-width="1.6"/></svg>
        elias@example.com
      </li>
      <li>
        <svg viewBox="0 0 16 16" aria-hidden="true"><circle cx="8" cy="8" r="6.5" fill="none" stroke="#1d4f8c" stroke-width="1.6"/><path d="M1.5 8h13M8 1.5c-3 3.5-3 9.5 0 13M8 1.5c3 3.5 3 9.5 0 13" fill="none" stroke="#1d4f8c" stroke-width="1.2"/></svg>
        harborrlumencapital.example.co.uk
      </li>
    </ul>

    <div class="brand">
      <span class="brand-mark"></span>
      <span class="brand-name">Harbor Lumen Capital</span>
    </div>

    <span class="band-blue"></span>
    <span class="band-red"></span>
  </section>

</main>
</body>
</html>
```